Fresh & Clean *NEW* BUSINESS CARD Needed - OPTOMETRY Clinic/Optical

High-tech optometry practice with 3 doctors seeking new business card.  We provide eye exams, sell, designer glasses/contacts/specialty eyewear and treat ocular diseases.  For our business cards, we are seeking fresh, clean, and crisp design as we grow our team (staffing change).  Simply adding doctors is making the card look busy/cluttered.
 Looking for professional, less cluttered look yet still have our logo, doctor names, phone, address, and website....If possible!  :)
Names:
Marcia Trelford, O.D.
Ned Pallister, O.D.
Oona Ferrant, O.D.
Phone: 555-014-2738
Website: www.BrightLensHub.example
Address:  417 Garnet R. Holloway, Fernwick, QA 00000
Ultimately we have the main business card with all doctor sames and that card has two versions  (front is always the same).  The back has two designs (1) displays next appointment time/date, (2) for "general use" (non-appointment.)    I have attached what we have used in the past.  
We also need a design template for each team member in our practice with their name, title, and email.   Those should be designed with the "general use" back (see attached).
**Open to entirely new design so don't feel obligated to keep current format.  Need new perspective!  Also including our watermark and some other design features we have consistently used in past in our portfolio.  Included are two options for logos--vertical and horizontal.
**I also would like to remove "Member of Sight Alliance" on our logo if possible**
 Other image files available upon request.

Target Market(s)

New patient & Current Patients

Industry/Entity Type

Optometry

Contact Information for Business Card

High-tech optometry practice with 3 doctors seeking new business card.  We provide eye exams, sell, designer glasses/contacts/specialty eyewear and treat ocular diseases.  For our business cards, we are seeking fresh, clean, and crisp design as we grow our team (staffing change).  Simply adding doctors is making the card look busy/cluttered.  Looking for professional, less cluttered look yet still have our logo, doctor names, phone, address, and website....If possible!  :) Names: Marcia Trelford, O.D. Ned Pallister, O.D. Oona Ferrant, O.D. Phone: 555-014-2738 Website: www.BrightLensHub.example Address:  417 Garnet R. Holloway, Fernwick, QA 00000 Ultimately we have the main business card with all doctor sames and that card has two versions  (front is always the same).  The back has two designs (1) displays next appointment time/date, (2) for "general use" (non-appointment.)    I have attached what we have used in the past.   We also need a design template for each team member in our practice with their name, title, and email.   Those should be designed with the "general use" back (see attached). **Open to entirely new design so don't feel obligated to keep current format.  Need new perspective!  Also including our watermark and some other design features we have consistently used in past in our portfolio.  Included are two options for logos--vertical and horizontal. **I also would like to remove "Member of Sight Alliance" on our logo if possible**  Other image files available upon request.

Font styles to use
Other font styles liked:
• We have used Montserrat / Yellowtail in the past

Colors

Designer to choose colors to be used in the design.

Requirements
Must have
• Clean & Fresh Design with Logo / Info provided in description. Horizontal orientation. **I have included the CMYK colors we currently have in our logo.
Should not have
• Cluttered

```html
<!DOCTYPE html>
<html lang="en">
<head>
<meta charset="utf-8">
<title>Bright Lens Hub – Business Cards</title>
<link href="https://fonts.googleapis.com/css2?family=Roboto:wght@400;500;700&display=swap" rel="stylesheet">
<style>
  :root {
    --backdrop: #3b3b3d;
    --gold: #dcb400;
    --card: #ffffff;
    --ink: #2e2e30;
    --ink-soft: #4a4a4d;
    --rule: #555558;
    --box-shade: #bbbbbb;
  }
  * { box-sizing: border-box; margin: 0; padding: 0; }
  html, body {
    width: 1200px; height: 694px; overflow: hidden;
    background: var(--backdrop);
    font-family: "Roboto", Arial, sans-serif;
    color: var(--ink);
  }
  .canvas { position: relative; width: 1200px; height: 694px; }
  .card {
    position: absolute; top: 187px;
    width: 540px; height: 320px;
    background: var(--gold);
    border-radius: 40px;
    padding: 12px;
  }
  .card--front { left: 40px; }
  .card--back { left: 620px; }
  .card__face {
    position: relative; width: 100%; height: 100%;
    background: var(--card);
    border-radius: 30px;
  }
  .brand {
    position: absolute;
    display: flex; align-items: center; gap: 14px;
    font-weight: 400; color: var(--ink);
    white-space: nowrap;
  }
  .brand__dot {
    width: 40px; height: 40px; border-radius: 50%;
    background: var(--gold); flex: none;
  }
  .card--front .brand { left: 40px; top: 38px; font-size: 36px; }
  .doctors {
    position: absolute; left: 46px; top: 150px;
    list-style: none; font-weight: 700; font-size: 18px; line-height: 27px;
    white-space: nowrap;
  }
  .doctors li { display: flex; align-items: center; gap: 12px; }
  .doctors li::before {
    content: ""; width: 8px; height: 8px; border-radius: 50%;
    background: var(--gold); flex: none;
  }
  .divider { position: absolute; width: 0; border-left: 2px dotted var(--rule); }
  .card--front .divider { left: 292px; top: 122px; height: 110px; }
  .contact { position: absolute; left: 316px; top: 122px; white-space: nowrap; }
  .contact__phone {
    display: flex; align-items: center; gap: 8px;
    font-size: 24px; font-weight: 500;
  }
  .contact__phone svg { width: 20px; height: 20px; fill: var(--ink); }
  .contact__address {
    margin-top: 6px; font-size: 13px; font-weight: 500;
    line-height: 17px; color: var(--ink-soft);
  }
  .website {
    position: absolute; right: 40px; bottom: 40px;
    font-size: 13px; font-weight: 500; white-space: nowrap;
  }
  .card--back .brand {
    left: 36px; top: 70px;
    flex-direction: column; align-items: flex-start; gap: 14px;
    font-size: 34px; line-height: 38px;
  }
  .card--back .brand__dot { width: 52px; height: 52px; }
  .card--back .divider { left: 252px; top: 36px; height: 160px; }
  .appointment { position: absolute; left: 276px; top: 36px; right: 32px; }
  .appointment__title { font-size: 19px; font-weight: 700; white-space: nowrap; }
  .field {
    display: flex; align-items: flex-end; gap: 8px;
    margin-top: 14px; font-size: 13px; font-weight: 500;
  }
  .field__line { flex: 1; border-bottom: 1.5px solid var(--ink); height: 14px; }
  .weekdays { display: flex; gap: 12px; margin-top: 20px; }
  .weekdays span {
    width: 22px; height: 22px; border: 1.5px solid var(--ink);
    box-shadow: 2px 2px 0 var(--box-shade);
    font-size: 11px; font-weight: 500;
    display: flex; align-items: center; justify-content: center;
  }
  .notice {
    position: absolute; left: 220px; right: 16px; bottom: 34px;
    text-align: center; font-size: 12px; font-weight: 700; line-height: 17px;
    white-space: nowrap;
  }
</style>
</head>
<body>
<main class="canvas">
  <section class="card card--front" aria-label="Card front">
    <div class="card__face">
      <div class="brand"><span class="brand__dot"></span>Bright Lens Hub</div>
      <ul class="doctors">
        <li>Marcia Trelford, O.D.</li>
        <li>Ned Pallister, O.D.</li>
        <li>Oona Ferrant, O.D.</li>
      </ul>
      <div class="divider"></div>
      <div class="contact">
        <p class="contact__phone">
          <svg viewBox="0 0 24 24" aria-hidden="true"><path d="M6.6 10.8a15.1 15.1 0 0 0 6.6 6.6l2.2-2.2a1 1 0 0 1 1-.25 11.4 11.4 0 0 0 3.6.57 1 1 0 0 1 1 1V20a1 1 0 0 1-1 1A17 17 0 0 1 3 4a1 1 0 0 1 1-1h3.5a1 1 0 0 1 1 1c0 1.25.2 2.45.57 3.57a1 1 0 0 1-.25 1z"/></svg>
          555-014-2738
        </p>
        <p class="contact__address">417 Garnet R. Holloway,<br>Fernwick, QA 00000</p>
      </div>
      <p class="website">www.BrightLensHub.example</p>
    </div>
  </section>

  <section class="card card--back" aria-label="Card back, appointment reminder">
    <div class="card__face">
      <div class="brand"><span class="brand__dot"></span><span>Bright Lens<br>Hub</span></div>
      <div class="divider"></div>
      <div class="appointment">
        <h2 class="appointment__title">Your Next Appointment</h2>
        <div class="field"><span>Date</span><span class="field__line"></span></div>
        <div class="field"><span>Time</span><span class="field__line"></span></div>
        <div class="weekdays">
          <span>M</span><span>T</span><span>W</span><span>T</span><span>F</span><span>S</span>
        </div>
      </div>
      <p class="notice">If your are unable to keep your appointment<br>please kindly give us 24 hour notice</p>
    </div>
  </section>
</main>
</body>
</html>
```